App UI Design: Shopping/E-commerce App

Project :
Develop an UI design & App icon for an E-commerce/Shopping App

About the App/ Target Audience:
This grocery & food shopping app will be used by independent pub, café, restaurant owners to place & manage their purchases of foods and groceries for their catering businesses.

They will use the app to access product catalogues & special promotions, search & buy large quantities of groceries or catering supplies, and the ability to manage and track status of their order.

The HTML5 App’s has been built with a very basic structure. It now needs the visual layer of the UI designed

Note:
The app is tailored for business & catering orders, not retail/supermarket buyers, so the visual needs to look smart & not too casual.
Updates

Reason: Current submissions have not met out expectations. Please use the similar app examples in the PDF as a strong point of reference for the look & feel. Feedback will be given as submissions come in, please feel free to submit initial concepts of 1 or 2 of the pages & we'll provide feedback on whether it is on the right track or not before you do more work. Current submission will also receive feedback in the next few days. We look forward to new submissions!

Target Market(s)

Male & Female. Independent pub, café, restaurant owners buying for their catering businesses. Chefs etc.

Industry/Entity Type

Restaurant

Requirements
Must have
• An overview of elements/pages of the app that needs to be designed are:
(DOWNLOAD a more detailed diagram PDF explanation)

1. Welcome- Log-in Page
2. Homepage – index that links to different function of the app

Products:
3. Promotions page – for products on special for a limited time
4. Catalogue page – access to a range of catalogue

Ways to buy:
5. Basket (Shopping Cart) - tracking items they are buying from the catalogues
6. Templates (Pre-set Shopping list)- Set shopping list that has been preloaded for certain menu
7. Open Order page

My Account:
8. My Account/profile page – Users can check the status of their order, look at past orders, look at their account number & details etc

_______________________________________________________

Icon set- Icons to represent each pages that act as visual cues for easier browsing.

2 Main features that need to be accessible & consistent throughout all pages are:
a) The Navigation Bar –
so the user can quickly find their way back & access to the main functions
b) The Search bar –
whether it drops down when needed, or is featured as a header/footer.
c) Log out button
Nice to have

Things to keep in mind:

The UI design essentially needs to be a customizable template that can easily adapt to any brand/logo with a slight change of the color scheme. As we will later implement our brand & logo onto it.

We’re looking for a clean & clear design that allows for a straight forward easy user experience.

You are free to develop different layout & UI pattern that you feel is the most efficient way the user can walk through the App & make their purchase in no more than 2 or 3 clicks
________________________________________________

Screenshot of Similar Apps for reference are also in the PDF

```html
<!DOCTYPE html>
<html lang="en">
<head>
<meta charset="utf-8">
<title>Product Details</title>
<link href="https://fonts.googleapis.com/css2?family=Arimo:wght@400;700&display=swap" rel="stylesheet">
<style>
  :root {
    --green-top: #23852f;
    --green-bottom: #0c5417;
    --green-dark: #0b5a19;
    --green-line: #0a4512;
    --status-bg: #2a2a2a;
    --white: #ffffff;
    --text-dark: #222222;
    --text-body: #555555;
    --rule: #d6d6d6;
    --panel: #efefef;
    --photo-a: #d9cfc6;
    --photo-b: #6b4a33;
    --photo-c: #f1ece6;
  }
  * { box-sizing: border-box; margin: 0; padding: 0; }
  html, body { width: 800px; height: 1200px; overflow: hidden; background: var(--white); }
  body { font-family: "Arimo", Arial, sans-serif; position: relative; color: var(--text-dark); }

  .status-bar {
    position: absolute; left: 0; top: 0; width: 800px; height: 53px;
    background: linear-gradient(#3a3a3a, #151515);
    color: var(--white); font-weight: 700; font-size: 34px;
    display: flex; align-items: center; justify-content: center;
  }
  .status-bar .signal { position: absolute; left: 14px; top: 18px; }
  .status-bar .battery { position: absolute; right: 14px; top: 17px; }

  .nav-bar {
    position: absolute; left: 0; top: 53px; width: 800px; height: 112px;
    background: linear-gradient(var(--green-top), var(--green-bottom));
    border-bottom: 2px solid var(--green-line);
  }
  .nav-btn {
    position: absolute; top: 0; height: 110px; width: 80px;
    display: flex; align-items: center; justify-content: center;
  }
  .nav-btn.back { left: 0; border-right: 2px solid var(--green-line); }
  .nav-btn.menu { left: 82px; width: 96px; border-right: 2px solid var(--green-line); }
  .nav-btn.search { right: 0; width: 96px; border-left: 2px solid var(--green-line); }
  .nav-title {
    position: absolute; left: 0; right: 0; top: 0; height: 110px;
    display: flex; align-items: center; justify-content: center;
    color: var(--white); font-weight: 700; font-size: 44px;
  }

  .product-photo {
    position: absolute; left: 0; top: 165px; width: 800px; height: 400px;
    background: radial-gradient(ellipse at 55% 60%, var(--photo-b) 0%, var(--photo-a) 45%, var(--photo-c) 100%);
  }

  .product-name {
    position: absolute; left: 0; right: 0; top: 585px;
    text-align: center; font-weight: 700; font-size: 31px;
  }
  .title-rule { position: absolute; left: 80px; right: 80px; top: 645px; border-top: 2px solid var(--rule); }
  .product-desc {
    position: absolute; left: 60px; right: 60px; top: 672px;
    text-align: center; font-size: 20.5px; line-height: 26px; color: var(--text-body);
  }

  .options { position: absolute; left: 0; top: 789px; width: 800px; height: 411px; background: var(--panel); border-top: 2px solid var(--rule); }
  .option-row { position: absolute; left: 0; width: 800px; height: 126px; border-bottom: 2px solid var(--rule); }
  .option-row.single { top: 0; }
  .option-row.case { top: 126px; }
  .option-price { position: absolute; left: 38px; top: 30px; font-weight: 700; font-size: 31px; }
  .option-qty { position: absolute; left: 38px; top: 70px; font-size: 22px; }
  .stepper { position: absolute; right: 30px; top: 40px; width: 210px; height: 52px; }
  .stepper-field {
    position: absolute; left: 44px; top: 4px; width: 122px; height: 44px;
    background: var(--white); border: 2px solid #cccccc;
    display: flex; align-items: center; justify-content: center; font-size: 27px;
  }
  .stepper svg { position: absolute; top: 0; }

  .add-button {
    position: absolute; left: 67px; top: 1072px; width: 666px; height: 101px;
    background: linear-gradient(#137226, var(--green-dark));
    border-radius: 6px;
    display: flex; align-items: center; justify-content: center; gap: 18px;
    color: var(--white); font-weight: 700; font-size: 38px;
  }
</style>
</head>
<body>
  <header class="status-bar">
    <svg class="signal" width="60" height="18" viewBox="0 0 60 18">
      <rect x="0" y="12" width="6" height="6" fill="#fff"/>
      <rect x="9" y="9" width="6" height="9" fill="#fff"/>
      <rect x="18" y="6" width="6" height="12" fill="#fff"/>
      <rect x="27" y="3" width="6" height="15" fill="#fff"/>
      <rect x="36" y="0" width="6" height="18" fill="#fff"/>
    </svg>
    <span>8:08 PM</span>
    <svg class="battery" width="62" height="22" viewBox="0 0 62 22">
      <rect x="1" y="1" width="54" height="20" rx="3" fill="none" stroke="#fff" stroke-width="2"/>
      <rect x="5" y="5" width="46" height="12" fill="#fff"/>
      <rect x="56" y="7" width="5" height="8" fill="#fff"/>
    </svg>
  </header>

  <nav class="nav-bar">
    <div class="nav-btn back">
      <svg width="26" height="36" viewBox="0 0 26 36"><path d="M20 4 L6 18 L20 32" fill="none" stroke="#fff" stroke-width="6" stroke-linecap="round" stroke-linejoin="round"/></svg>
    </div>
    <div class="nav-btn menu">
      <svg width="44" height="36" viewBox="0 0 44 36"><rect y="2" width="44" height="6" rx="2" fill="#fff"/><rect y="15" width="44" height="6" rx="2" fill="#fff"/><rect y="28" width="44" height="6" rx="2" fill="#fff"/></svg>
    </div>
    <h1 class="nav-title">Product Details</h1>
    <div class="nav-btn search">
      <svg width="44" height="44" viewBox="0 0 44 44"><circle cx="18" cy="18" r="13" fill="none" stroke="#fff" stroke-width="6"/><line x1="28" y1="28" x2="40" y2="40" stroke="#fff" stroke-width="7" stroke-linecap="round"/></svg>
    </div>
  </nav>

  <div class="product-photo" role="img" aria-label="Photo of a mocha cake topped with cream, strawberry, kiwi and orange slices and chocolate shards"></div>

  <h2 class="product-name">Organic Fruity Mocca Cake</h2>
  <div class="title-rule"></div>
  <p class="product-desc">Start new healthy life with this organic cake created with mocca and fresh fruits inside, tasty and healthy. The promotion for the price discount and few bonus, so buy it now!</p>

  <section class="options">
    <div class="option-row single">
      <div class="option-price">Single: $20</div>
      <div class="option-qty">Order quantity : 2</div>
      <div class="stepper">
        <svg style="left:0" width="52" height="52" viewBox="0 0 52 52"><circle cx="26" cy="26" r="24" fill="#0e5e1b"/><rect x="13" y="22" width="26" height="8" fill="#fff"/></svg>
        <div class="stepper-field">1</div>
        <svg style="left:158px" width="52" height="52" viewBox="0 0 52 52"><circle cx="26" cy="26" r="24" fill="#0e5e1b"/><rect x="13" y="22" width="26" height="8" fill="#fff"/><rect x="22" y="13" width="8" height="26" fill="#fff"/></svg>
      </div>
    </div>
    <div class="option-row case">
      <div class="option-price">Case: $35</div>
      <div class="option-qty">Order quantity : 3</div>
      <div class="stepper">
        <svg style="left:0" width="52" height="52" viewBox="0 0 52 52"><circle cx="26" cy="26" r="24" fill="#0e5e1b"/><rect x="13" y="22" width="26" height="8" fill="#fff"/></svg>
        <div class="stepper-field">1</div>
        <svg style="left:158px" width="52" height="52" viewBox="0 0 52 52"><circle cx="26" cy="26" r="24" fill="#0e5e1b"/><rect x="13" y="22" width="26" height="8" fill="#fff"/><rect x="22" y="13" width="8" height="26" fill="#fff"/></svg>
      </div>
    </div>
  </section>

  <div class="add-button">
    <svg width="44" height="40" viewBox="0 0 44 40">
      <path d="M12 16 L20 4 M32 16 L24 4" stroke="#fff" stroke-width="4" stroke-linecap="round"/>
      <rect x="1" y="14" width="42" height="7" rx="2" fill="#fff"/>
      <path d="M5 23 H39 L35 38 H9 Z" fill="#fff"/>
      <path d="M15 26 V35 M22 26 V35 M29 26 V35" stroke="#0b5a19" stroke-width="3"/>
    </svg>
    <span>Add to Basket</span>
  </div>
</body>
</html>
```